Business Cards for company that supports physicians that do medical research

Need to create a business card for Norvale Studies (www.norvalestudies.example), a company devoted to supporting physicians who conduct medical research. The form of the card should match the message of research and information quest. I have provided the logo of the company as an uploaded file. Designs should be simple and slick aimed at very high end clients.

Target Market(s)

Medical doctors that are also researchers

Industry/Entity Type

Medical

Contact Information for Business Card

Should feature logo and fields for personal info:
Name/title
Phone /email

Font styles to use
Serif
Sans Serif

Requirements
Must have
• Norvale logo and fields for personal info:
• Name: Corwin Abbatelli
• Title: VP Research and Senior Analyst
• Phone: 555-203-7416
• email: info@norvalestudies.example
Nice to have
• Interesting cards that I've seen:
• 1- all black/charcoal or very dark background
• 2- Plastic - semi-transparent
• 3- non-standard height-width ratios
• 4- Functional cards -- USB drive incorporated
Should not have
• Too busy; needs to stay very simple

```html
<!DOCTYPE html>
<html lang="en">
<head>
<meta charset="utf-8">
<title>Norvale Studies – Business Card</title>
<link rel="stylesheet" href="https://fonts.googleapis.com/css2?family=Open+Sans:wght@400;600;700&display=swap">
<style>
  :root {
    --stage: #3b3431;
    --card-dark: #1f1f20;
    --card-blue: #2b86cf;
    --accent-green: #5cbf3f;
    --accent-blue: #2f8fd6;
    --text-light: #e8e8e8;
    --divider: #3a3a3b;
    --white: #ffffff;
  }
  * { box-sizing: border-box; margin: 0; padding: 0; }
  html, body {
    width: 1200px; height: 844px; overflow: hidden;
    background: var(--stage);
    font-family: "Open Sans", Arial, sans-serif;
  }
  .stage {
    width: 1200px; height: 844px;
    display: flex; align-items: center; justify-content: center; gap: 40px;
  }
  .card {
    width: 540px; height: 309px; position: relative; flex: none;
    border-radius: 3px;
    box-shadow: 0 10px 30px rgba(0,0,0,.45);
  }

  /* Front: dark card */
  .card--front { background: var(--card-dark); display: flex; }
  .brand {
    width: 280px; padding: 0 0 0 26px;
    display: flex; align-items: center; gap: 10px;
  }
  .brand__dot {
    width: 20px; height: 20px; border-radius: 50%;
    background: var(--accent-blue); flex: none;
  }
  .brand__name {
    font-size: 25px; font-weight: 600; color: var(--accent-green);
    white-space: nowrap;
  }
  .details {
    flex: 1; border-left: 1px solid var(--divider);
    margin: 72px 0; padding: 4px 16px 0 22px;
  }
  .details__name {
    font-size: 18px; font-weight: 700; color: var(--accent-green);
    white-space: nowrap;
  }
  .details__title {
    font-size: 12.5px; color: var(--text-light); margin-top: 2px;
    white-space: nowrap;
  }
  .contact { list-style: none; margin-top: 22px; }
  .contact li {
    display: flex; align-items: center; gap: 9px;
    font-size: 13.5px; color: var(--text-light); margin-bottom: 6px;
    white-space: nowrap;
  }
  .contact svg { width: 11px; height: 11px; flex: none; }
  .icon-phone { fill: var(--accent-green); }
  .icon-mail { fill: none; stroke: var(--accent-green); stroke-width: 2.4; stroke-linejoin: round; }

  /* Back: blue card */
  .card--back {
    background: var(--card-blue);
    display: flex; align-items: center; justify-content: center;
  }
  .back-brand { display: flex; align-items: center; gap: 14px; margin-top: -30px; }
  .back-brand__dot { width: 24px; height: 24px; border-radius: 50%; background: var(--white); flex: none; }
  .back-brand__name {
    font-size: 34px; font-weight: 600; color: var(--white); white-space: nowrap;
  }
  .website {
    position: absolute; bottom: 62px; right: 92px;
    font-size: 13px; font-weight: 700; color: var(--white); white-space: nowrap;
  }
</style>
</head>
<body>
  <main class="stage">
    <section class="card card--front" aria-label="Card front">
      <div class="brand">
        <span class="brand__dot"></span>
        <span class="brand__name">Norvale Studies</span>
      </div>
      <div class="details">
        <p class="details__name">Corwin Abbatelli</p>
        <p class="details__title">VP Research and Senior Analyst</p>
        <ul class="contact">
          <li>
            <svg class="icon-phone" viewBox="0 0 24 24" aria-hidden="true"><path d="M6.6 10.8a15.1 15.1 0 0 0 6.6 6.6l2.2-2.2c.3-.3.7-.4 1-.2 1.1.4 2.3.6 3.6.6.6 0 1 .4 1 1V20c0 .6-.4 1-1 1C10.6 21 3 13.4 3 4c0-.6.4-1 1-1h3.5c.6 0 1 .4 1 1 0 1.3.2 2.5.6 3.6.1.3 0 .7-.2 1z"/></svg>
            555-203-7416
          </li>
          <li>
            <svg class="icon-mail" viewBox="0 0 24 24" aria-hidden="true"><rect x="2.5" y="5" width="19" height="14"/><path d="M2.5 5l9.5 8 9.5-8"/></svg>
            info@norvalestudies.example
          </li>
        </ul>
      </div>
    </section>

    <section class="card card--back" aria-label="Card back">
      <div class="back-brand">
        <span class="back-brand__dot"></span>
        <span class="back-brand__name">Norvale Studies</span>
      </div>
      <p class="website">www.norvalestudies.example</p>
    </section>
  </main>
</body>
</html>
```